Electrical company business card design.

Hi, were an electrical company in Auckland New Zealand called Quarneth Ltd. We focus mainly on high end residential and commercial so the card would be targeted towards that.
The card will be for myself, i am the director of the company.
Name: Derek Olstow
Position: Director/electrician
Phone: 021 387 9415
Email: derek@quarneth.co.nz
Location: Auckland
As for colors the the blue color in the logo is preferred, i also don't mind a black background option.
Target Market(s)
High end residential and commercial
Industry/Entity Type
Electrician
Contact Information for Business Card
Name: Derek Olstow Position: Director/Electrician Phone: 021 387 9415, Email: derek@quarneth.co.nz, Location: Auckland

```html
<!DOCTYPE html>
<html lang="en">
<head>
<meta charset="utf-8">
<title>Quarneth Ltd — Business Card</title>
<link href="https://fonts.googleapis.com/css2?family=Inter:wght@400;600;700&family=Montserrat:wght@500;700&display=swap" rel="stylesheet">
<style>
  :root{
    --stage:#acacac;
    --blue-light:#0b88cc;
    --blue-deep:#005aa7;
    --blue-text:#0f7cc4;
    --ink:#4a4f54;
    --ink-soft:#5a5f64;
    --white:#ffffff;
    --rule:#9a9a9a;
  }
  *{margin:0;padding:0;box-sizing:border-box}
  html,body{width:1200px;height:1000px;overflow:hidden;background:var(--stage)}
  .canvas{position:relative;width:1200px;height:1000px}
  .card{position:absolute;left:248px;width:694px;height:400px;border-radius:27px;
    box-shadow:6px 8px 12px rgba(70,55,50,.35)}
  .card--front{top:75px;
    background:linear-gradient(135deg,var(--blue-light) 0%,#0574bd 45%,var(--blue-deep) 100%)}
  .card--back{top:517px;background:var(--white)}

  .brand{position:absolute;font-family:"Montserrat",sans-serif;font-weight:500;letter-spacing:.02em}
  .brand__name{display:flex;align-items:center;gap:10px}
  .brand__mark{display:inline-block;background:var(--white)}
  .brand__tagline{font-family:"Montserrat",sans-serif;font-weight:700;letter-spacing:.06em;white-space:nowrap}

  .card--front .brand{right:62px;bottom:50px;color:var(--white);text-align:right}
  .card--front .brand__name{font-size:34px;line-height:1;justify-content:flex-end}
  .card--front .brand__mark{width:18px;height:18px}
  .card--front .brand__tagline{font-size:10.5px;margin-top:6px}

  .card--back .brand{left:80px;top:130px;width:252px;color:var(--ink);text-align:center}
  .card--back .brand__mark{display:block;width:36px;height:36px;background:var(--blue-text);margin:0 auto 40px}
  .card--back .brand__name{display:block;font-size:44px;line-height:1;letter-spacing:0}
  .card--back .brand__tagline{font-size:15px;margin-top:12px}

  .contact{position:absolute;left:396px;top:148px;font-family:"Inter",sans-serif;color:var(--ink-soft)}
  .contact__name{font-size:24px;font-weight:700;color:var(--ink);line-height:1.1}
  .contact__first{color:var(--blue-text)}
  .contact__role{font-size:14px;margin-top:4px}
  .contact__rule{width:174px;height:1px;background:var(--rule);margin:10px 0 12px}
  .contact__row{display:flex;align-items:center;gap:9px;font-size:20px;line-height:1.45}
  .contact__icon{width:16px;height:16px;fill:var(--blue-text);flex:none}
</style>
</head>
<body>
<div class="canvas">
  <section class="card card--front" aria-label="Card front">
    <div class="brand">
      <div class="brand__name"><span class="brand__mark"></span>QUARNETH</div>
      <div class="brand__tagline">ENERGY WITH ACCURACY</div>
    </div>
  </section>

  <section class="card card--back" aria-label="Card back">
    <div class="brand">
      <span class="brand__mark"></span>
      <div class="brand__name">QUARNETH</div>
      <div class="brand__tagline">ENERGY WITH ACCURACY</div>
    </div>

    <div class="contact">
      <div class="contact__name"><span class="contact__first">Derek</span> Olstow</div>
      <div class="contact__role">Director/electrician</div>
      <div class="contact__rule"></div>
      <div class="contact__row">
        <svg class="contact__icon" viewBox="0 0 24 24" aria-hidden="true"><path d="M6.6 10.8a15.1 15.1 0 0 0 6.6 6.6l2.2-2.2a1 1 0 0 1 1-.25 11.4 11.4 0 0 0 3.6.57 1 1 0 0 1 1 1V20a1 1 0 0 1-1 1A17 17 0 0 1 3 4a1 1 0 0 1 1-1h3.5a1 1 0 0 1 1 1c0 1.25.2 2.45.57 3.570a1 1 0 0 1-.25 1z"/></svg>
        021 387 9415
      </div>
      <div class="contact__row">
        <svg class="contact__icon" viewBox="0 0 24 24" aria-hidden="true"><path d="M12 2a7 7 0 0 0-7 7c0 5.2 7 13 7 13s7-7.8 7-13a7 7 0 0 0-7-7zm0 9.5A2.5 2.5 0 1 1 12 6.5a2.5 2.5 0 0 1 0 5z"/></svg>
        Auckland
      </div>
    </div>
  </section>
</div>
</body>
</html>
```